Letterhead Design Project

I need letterhead designed for my law firm. It would also be used for web based stuff as well.

Industry/Entity Type

Law Firm

```html
<!DOCTYPE html>
<html lang="en">
<head>
<meta charset="utf-8">
<title>Hartwell &amp; Osei — Stationery</title>
<link href="https://fonts.googleapis.com/css2?family=Josefin+Slab:wght@400;600&display=swap" rel="stylesheet">
<style>
  :root {
    --backdrop: #2c2c2c;
    --stock-black: #1a1a1a;
    --stock-black-soft: #222222;
    --stock-white: #ffffff;
    --band-grey: #3f3f3f;
    --ink: #3a3a3a;
    --ink-muted: #555555;
    --ornament: #4a4a4a;
  }
  * { box-sizing: border-box; margin: 0; padding: 0; }
  html, body { width: 1200px; height: 848px; overflow: hidden; }
  body {
    background: var(--backdrop);
    font-family: "Josefin Slab", Georgia, serif;
    position: relative;
  }
  .business-card {
    position: absolute; left: 58px; top: 87px; width: 546px; height: 262px;
    background: var(--stock-black);
  }
  .business-card .firm-name {
    position: absolute; left: 0; right: 0; top: 112px;
    text-align: center; font-size: 30px; line-height: 36px; font-weight: 600;
    color: var(--ink-muted); letter-spacing: 1px;
  }
  .envelope {
    position: absolute; left: 58px; top: 400px; width: 546px; height: 338px;
  }
  .envelope-back {
    position: absolute; inset: 0;
    background: var(--stock-black-soft); border-radius: 10px 10px 0 0;
  }
  .envelope-letter {
    position: absolute; left: 6px; right: 6px; top: 66px; height: 64px;
    background: var(--stock-white); overflow: hidden;
  }
  .envelope-letter svg { position: absolute; left: 0; top: 0; }
  .envelope-letter .firm-name {
    position: absolute; left: 0; right: 0; top: 31px; text-align: center;
    font-size: 22px; line-height: 26px; font-weight: 600; color: var(--ink);
  }
  .envelope-pocket {
    position: absolute; left: 0; right: 0; top: 130px; bottom: 0;
    background: var(--stock-black);
  }
  .letterhead {
    position: absolute; left: 619px; top: 78px; width: 510px; height: 721px;
    background: var(--stock-white); color: var(--ink);
  }
  .letterhead-header { position: absolute; left: 0; top: 0; }
  .letterhead .firm-name {
    position: absolute; left: 0; right: 0; top: 48px; text-align: center;
    font-size: 21px; line-height: 26px; font-weight: 600; color: var(--ink);
  }
  .letter-body {
    position: absolute; left: 71px; top: 206px; width: 368px;
    font-size: 9.4px; line-height: 12.9px; text-align: justify;
  }
  .letter-body p { margin-bottom: 12.9px; }
  .contact {
    position: absolute; left: 0; right: 0; top: 631px;
    text-align: center; font-size: 9.4px; line-height: 12.5px; font-weight: 600;
  }
  .footer-rule { position: absolute; left: 0; top: 670px; }
</style>
</head>
<body>

<section class="business-card">
  <div class="firm-name">Hartwell &amp; Osei</div>
</section>

<section class="envelope">
  <div class="envelope-back"></div>
  <div class="envelope-letter">
    <svg width="534" height="64" viewBox="0 0 534 64">
      <rect x="0" y="29" width="534" height="35" fill="var(--band-grey)"/>
      <polygon points="145,29 389,29 403,46 389,64 145,64 131,46" fill="var(--stock-white)"/>
    </svg>
    <div class="firm-name">Hartwell &amp; Osei</div>
  </div>
  <div class="envelope-pocket"></div>
</section>

<section class="letterhead">
  <svg class="letterhead-header" width="510" height="150" viewBox="0 0 510 150">
    <polygon points="0,33 139,33 125,61 139,89 0,89" fill="var(--band-grey)"/>
    <polygon points="371,33 510,33 510,89 371,89 385,61" fill="var(--band-grey)"/>
    <polygon points="243,100 267,100 267,142 255,133 243,142" fill="var(--band-grey)"/>
  </svg>
  <div class="firm-name">Hartwell &amp; Osei</div>

  <div class="letter-body">
    <p>Lorem ipsum dolor sit amet,</p>
    <p>Lorem ipsum dolor sit amet, consectetur adipiscing elit. Donec orci purus, luctus vitae dignissim eu, iaculis sed purus. Vivamus faucibus, ipsum nec aliquet viverra, leo mauris condimentum ligula, sit amet sagittis enim ligula quis arcu. Nam egestas tortor id nisi porttitor mattis. In tortor ante, ultricies in suscipit a, tempus non massa. Vivamus et auctor mi. Fusce vel massa nulla. Phasellus nec eros mauris, et scelerisque orci. Donec malesuada orci vitae nulla accumsan porta a id massa. Quisque accumsan iaculis magna sit amet fringilla. Maecenas consequat, magna eget tincidunt semper, odio nibh rutrum mi, id feugiat ante nisi eu risus. Vestibulum nunc orci, rhoncus a placerat in, ultricies in mi. Cras mattis varius eros, vel fringilla nisi suscipit eget.</p>
    <p>Quisque scelerisque sagittis nulla at porttitor. Mauris a justo et tellus interdum tristique. Sed id augue vitae urna euismod commodo aliquet a quam. Pellentesque arcu velit, cursus et malesuada ut, consequat et diam. Nullam erat sem, rhoncus id ullamcorper vitae, rhoncus et arcu. In ultricies ultricies nulla, ut rutrum nisi iaculis at. Donec eu magna a metus ornare faucibus. Fusce aliquet faucibus ultricies. Morbi semper, est id tincidunt gravida, sem arcu adipiscing lacus, ac bibendum nulla leo eu purus. Quisque nec diam sed risus consectetur a ccumsan quis quis nibh. Vestibulum id purus lorem.</p>
    <p>Vivamus vehicula accumsan lacinia. Aliquam erat volutpat. Pellentesque consequat venenatis velit non gravida. Etiam et sem et nulla congue aliquam sed eget augue. Nulla facilisi. Pellentesque habitant morbi tristique senectus et netus et malesuada fames ac turpis egestas. Nulla a elit at sem iaculis congue. Nullam mollis tristique lobortis.</p>
  </div>

  <div class="contact">
    (912) 555-0187<br>
    office@hartwellosei.law<br>
    hartwellosei.law
  </div>

  <svg class="footer-rule" width="510" height="30" viewBox="0 0 510 30">
    <rect x="10" y="6" width="24" height="18" fill="var(--ornament)" role="img" aria-label="Corner flourish ornament"/>
    <rect x="476" y="6" width="24" height="18" fill="var(--ornament)" role="img" aria-label="Corner flourish ornament"/>
    <line x1="36" y1="16" x2="474" y2="16" stroke="var(--ink)" stroke-width="1" stroke-dasharray="4 3"/>
    <rect x="225" y="10" width="60" height="12" fill="var(--ornament)" role="img" aria-label="Centre scroll ornament"/>
  </svg>
</section>

</body>
</html>
```